Leadership Seminar Concept

We want the theme picture/design of the Leadership Seminar Flyer with theme "Inspiring Commitment"

Industry/Entity Type

Leadership

```html
<!DOCTYPE html>
<html lang="en">
<head>
<meta charset="utf-8">
<title>Inspiring Commitment – Leadership Seminar Flyer</title>
<link href="https://fonts.googleapis.com/css2?family=Arimo:wght@400;700&family=Open+Sans:wght@400;700&family=Dancing+Script:wght@500&display=swap" rel="stylesheet">
<style>
  :root {
    --page-bg: #e9e9ea;
    --navy-deep: #0f2038;
    --navy: #1c3150;
    --steel: #5d7a98;
    --glow: #fff3d6;
    --amber: #e9b980;
    --haze: #a9bdd0;
    --white: #ffffff;
    --yellow: #f3e80f;
    --banner: #0a1630;
    --frame: rgba(255,255,255,0.75);
  }
  * { box-sizing: border-box; margin: 0; padding: 0; }
  html, body { width: 1200px; height: 1200px; overflow: hidden; background: var(--page-bg); }
  .flyer {
    position: absolute; left: 75px; top: 250px; width: 1050px; height: 700px;
    overflow: hidden; box-shadow: 0 10px 30px rgba(0,0,0,0.25);
    background: var(--navy-deep);
  }
  .flyer__scene {
    position: absolute; inset: 0;
    background:
      radial-gradient(ellipse 32% 30% at 62% 58%, var(--glow) 0%, rgba(255,236,200,0.85) 30%, rgba(233,185,128,0.45) 60%, rgba(233,185,128,0) 100%),
      radial-gradient(ellipse 60% 40% at 40% 85%, rgba(169,189,208,0.8) 0%, rgba(169,189,208,0) 100%),
      linear-gradient(180deg, var(--navy-deep) 0%, var(--navy) 30%, var(--steel) 62%, var(--haze) 80%, var(--steel) 100%);
  }
  .title-frame {
    position: absolute; left: 50px; top: 40px; width: 680px; height: 150px;
    border: 1.5px solid var(--frame);
  }
  .title {
    position: absolute; left: 150px; top: 78px;
    font-family: "Arimo", Arial, sans-serif; font-weight: 400;
    font-size: 44px; letter-spacing: 1px; color: var(--white);
  }
  .subtitle {
    position: absolute; left: 160px; top: 130px;
    font-family: "Arimo", Arial, sans-serif; font-weight: 700;
    font-size: 12px; color: var(--white);
  }
  .points { position: absolute; left: 50px; top: 215px; width: 680px; list-style: none; }
  .point { position: relative; padding-left: 45px; margin-bottom: 22px;
    font-family: "Open Sans", Arial, sans-serif; font-size: 15px; line-height: 1.35; color: var(--white); }
  .point__arrow { position: absolute; left: 0; top: 24px; width: 16px; height: 14px; }
  .point__lead { color: var(--yellow); font-weight: 700; }
  .invite {
    position: absolute; left: 110px; bottom: 35px; width: 770px; height: 105px;
    background: var(--banner); border-radius: 14px;
    display: flex; align-items: center; justify-content: center; text-align: center;
    font-family: "Dancing Script", cursive; font-size: 28px; line-height: 1.2; color: var(--yellow);
    padding: 0 30px;
  }
</style>
</head>
<body>
  <main class="flyer">
    <div class="flyer__scene" role="img" aria-label="Photo of a businessman with a briefcase looking over a city skyline at sunrise, reflected in water"></div>

    <div class="title-frame"></div>
    <h1 class="title">INSPIRING COMMITMENT</h1>
    <p class="subtitle">Shifting self, your people and your organization from static to movement to momentum</p>

    <ul class="points">
      <li class="point">
        <svg class="point__arrow" viewBox="0 0 16 14"><path d="M0 0 L16 7 L0 14 L5 7 Z" fill="#f3e80f"/></svg>
        <span class="point__lead">Inspiring commitment is enabling others to act.</span><br>
        It involves energizing individuals to strive towards a compelling vision of the future, guiding people through change, keeping everyone aligned, building trust and open channels of communication, while reinforcing success.
      </li>
      <li class="point">
        <svg class="point__arrow" viewBox="0 0 16 14"><path d="M0 0 L16 7 L0 14 L5 7 Z" fill="#f3e80f"/></svg>
        <span class="point__lead">Shiftability is responding to outward demands from inward strength, purpose and skill.</span><br>
        The mindset of shiftability acknowledges the need for change and embraces it, keeping an open mind about new ideas while wisely retaining things that still apply – always learning, always building, always growing.
      </li>
    </ul>

    <p class="invite">We invite you to a journey of greatness where you'll learn and practice tools for thriving as a leader by inspiring momentum.</p>
  </main>
</body>
</html>
```